4 x Florist Footpath Signage Boards that are consistant with each other for a modern florist

Eye catching, easy to read. little bit floral.
See example attached for wording. We are a modern florist in a country town.
This will be out on the street and needs to stand out!!

The Signage Panels
1. Valentines Day - 14th Feb
2. Workshop Signage boards - see attached example
3. Mothers Day Signage Board - 'Treat mum this Mothers Day'
4. We Are Open

Attached is a copy of the design guidelines and the template. the base of the sign is white.

Target Market(s)

Modern

Industry/Entity Type

Florist

Font styles to use
Sans Serif

Colors
eea4c8
f59296
ffffff
757575

Requirements
Must have
• flowers
• weddings
• giftware
• workshops
• flowers make people happy
• odettemarshpetals.co.nz
Nice to have
• Logo
• little bit of floral or greenery
• my shop is modem and industrial
Should not have
• Needs to be able to read easy

```html
<!DOCTYPE html>
<html lang="en">
<head>
<meta charset="utf-8">
<title>Valentines Day Footpath Sign</title>
<link rel="stylesheet" href="https://fonts.googleapis.com/css2?family=Great+Vibes&family=Libre+Baskerville:wght@400;700&display=swap">
<style>
  :root {
    --stage: #ececec;
    --board-white: #ffffff;
    --blush: #f8e9f8;
    --rose: #f3a3a6;
    --rose-soft: #f2b2c0;
    --rose-deep: #b23a5a;
    --leaf: #a9c4a4;
    --cream: #f7e6cf;
    --gold: #a8894f;
    --valentine-red: #e3121b;
    --violet: #5a3aa6;
    --violet-line: #8a6fc8;
  }
  * { box-sizing: border-box; margin: 0; padding: 0; }
  html, body { width: 720px; height: 1200px; overflow: hidden; }
  body { background: var(--stage); position: relative; }

  .sign-board {
    position: absolute; left: 24px; top: 150px;
    width: 672px; height: 900px;
    background: var(--blush);
    border-radius: 22px 22px 0 0;
    overflow: hidden;
    box-shadow: 0 6px 18px rgba(0,0,0,.18);
  }
  .floral-frame {
    position: absolute; inset: 0;
    background:
      radial-gradient(circle at 95px 80px, var(--rose) 0, rgba(243,163,166,.6) 60px, rgba(243,163,166,0) 120px),
      radial-gradient(circle at 250px 75px, var(--rose) 0, rgba(243,163,166,.55) 55px, rgba(243,163,166,0) 115px),
      radial-gradient(circle at 500px 80px, var(--rose-soft) 0, rgba(242,178,192,.55) 50px, rgba(242,178,192,0) 105px),
      radial-gradient(circle at 615px 70px, var(--rose-deep) 0, rgba(178,58,90,.5) 45px, rgba(178,58,90,0) 95px),
      radial-gradient(circle at 560px 170px, var(--cream) 0, rgba(247,230,207,0) 70px),
      radial-gradient(circle at 50px 260px, var(--leaf) 0, rgba(169,196,164,.4) 50px, rgba(169,196,164,0) 120px),
      radial-gradient(circle at 640px 300px, var(--leaf) 0, rgba(169,196,164,.35) 40px, rgba(169,196,164,0) 100px),
      radial-gradient(circle at 30px 620px, var(--leaf) 0, rgba(169,196,164,0) 80px),
      radial-gradient(circle at 650px 700px, var(--leaf) 0, rgba(169,196,164,0) 80px),
      radial-gradient(circle at 60px 800px, var(--cream) 0, rgba(247,230,207,.5) 50px, rgba(247,230,207,0) 100px),
      radial-gradient(circle at 150px 880px, var(--rose) 0, rgba(243,163,166,.5) 45px, rgba(243,163,166,0) 95px),
      radial-gradient(circle at 300px 820px, var(--leaf) 0, rgba(169,196,164,.4) 50px, rgba(169,196,164,0) 110px),
      radial-gradient(circle at 470px 840px, var(--rose) 0, rgba(243,163,166,.55) 60px, rgba(243,163,166,0) 125px),
      radial-gradient(circle at 630px 780px, var(--rose-soft) 0, rgba(242,178,192,0) 80px);
  }
  .carry-slot {
    position: absolute; left: 50%; top: 22px; transform: translateX(-50%);
    width: 104px; height: 24px; border-radius: 12px;
    background: var(--board-white); border: 2px solid #d8d0d8;
  }

  .brand-name {
    position: absolute; left: 0; top: 262px; width: 100%;
    text-align: center;
    font-family: "Libre Baskerville", serif; font-weight: 400;
    font-size: 16px; letter-spacing: 5px; line-height: 22px;
    color: var(--gold);
  }

  .event-title {
    position: absolute; left: 0; top: 420px; width: 100%;
    text-align: center;
    font-family: "Great Vibes", cursive; font-weight: 400;
    font-size: 104px; line-height: 120px;
    color: var(--valentine-red);
  }
  .event-date {
    position: absolute; left: 0; top: 540px; width: 100%;
    display: flex; align-items: center; justify-content: center; gap: 26px;
  }
  .event-date .rule { width: 120px; height: 2px; background: var(--gold); }
  .event-date .date-text {
    font-family: "Great Vibes", cursive; font-size: 58px; line-height: 64px;
    color: var(--violet);
  }

  .shop-online {
    position: absolute; left: 0; top: 654px; width: 100%; height: 36px;
    display: flex; align-items: center; justify-content: center; gap: 18px;
  }
  .shop-online .rule { width: 118px; height: 1px; background: var(--violet-line); }
  .shop-online .label {
    font-family: "Libre Baskerville", serif; font-weight: 700;
    font-size: 25px; color: var(--gold);
  }
  .web-address {
    position: absolute; left: 36px; top: 692px; width: 600px; height: 56px;
    border: 1px solid var(--violet-line); border-radius: 8px;
    display: flex; align-items: center; justify-content: center;
    font-family: "Libre Baskerville", serif; font-weight: 400;
    font-size: 27px; letter-spacing: 1.5px; color: var(--valentine-red);
  }
</style>
</head>
<body>
  <main class="sign-board">
    <div class="floral-frame" role="img" aria-label="Watercolour pink and burgundy roses, cream blossoms and soft greenery framing the board"></div>
    <div class="carry-slot"></div>

    <p class="brand-name">ODETTE<br>MARSH<br>PETALS</p>

    <h1 class="event-title">Valentines Day</h1>
    <div class="event-date">
      <span class="rule"></span>
      <span class="date-text">14th Feb</span>
      <span class="rule"></span>
    </div>

    <div class="shop-online">
      <span class="rule"></span>
      <span class="label">SHOP ONLINE</span>
      <span class="rule"></span>
    </div>
    <p class="web-address">OdetteMarshPetals.co.nz</p>
  </main>
</body>
</html>
```